Amber Ridge Publishing Web Page Design

Design a website for my new start up publishing company - Amber Ridge Publishing, the first work published by ARP with be a new book by M.R. Theodor called Silent Ledger. The prototype for the book cover is attached.

Target Market(s)

Worldwide, all readers of mystery, fiction, etc.

Industry/Entity Type

Book Publisher

Coding

Coded - Design and coding required

Number of Pages Required

1 page

```html
<!DOCTYPE html>
<html lang="en">
<head>
<meta charset="utf-8">
<title>Amber Ridge Publishing – Web Page Design</title>
<link href="https://fonts.googleapis.com/css2?family=Raleway:wght@400;500;600;700&display=swap" rel="stylesheet">
<style>
:root{
  --orange:#f7941d;
  --orange-deep:#e8850f;
  --ink:#222222;
  --dark:#2b2b2b;
  --darker:#1d1d1d;
  --grey:#8a8a8a;
  --light:#f4f4f4;
  --stage:#e6e6e6;
  --white:#ffffff;
}
*{box-sizing:border-box;margin:0;padding:0}
html,body{width:1200px;height:600px;overflow:hidden}
body{background:var(--stage);font-family:"Raleway",Arial,sans-serif;color:var(--ink);position:relative}
.panel{position:absolute;top:80px;height:440px;background:var(--white);overflow:hidden;box-shadow:0 6px 18px rgba(0,0,0,.18)}

/* Home panel */
.home{left:20px;width:520px}
.topbar{height:14px;background:var(--dark);color:#ccc;font-size:6px;display:flex;align-items:center;justify-content:space-between;padding:0 8px;white-space:nowrap}
.topbar .contact{display:flex;align-items:center;gap:8px}
.topbar .social{display:flex;gap:4px;align-items:center}
.topbar .social i{width:6px;height:6px;background:#bbb;display:block}
.nav{height:30px;display:flex;align-items:center;background:var(--white)}
.brand{background:var(--orange);color:var(--white);height:30px;display:flex;align-items:center;gap:5px;padding:0 9px;font-weight:700;font-size:9px;letter-spacing:.5px;line-height:1.05}
.brand i{width:10px;height:10px;border:1.5px solid var(--white);display:block}
.menu{display:flex;gap:10px;margin-left:12px;font-size:6.5px;font-weight:600;color:#555}
.menu .active{color:var(--orange)}
.menu-search{margin-left:auto;margin-right:8px;width:14px;height:14px;background:var(--orange)}
.hero{height:190px;background:
  radial-gradient(ellipse at 80% 30%,rgba(150,120,90,.45),transparent 55%),
  radial-gradient(ellipse at 20% 80%,rgba(110,95,80,.5),transparent 60%),
  linear-gradient(120deg,#3a3530,#1f1d1b 60%,#2d2a27);position:relative;color:var(--white)}
.hero-inner{position:absolute;left:70px;top:58px}
.hero .kicker{font-size:10px;font-weight:500}
.hero h1{font-size:22px;font-weight:600;letter-spacing:.5px;margin:2px 0 4px}
.hero p{font-size:6px;color:#ddd;max-width:210px;line-height:1.4}
.hero .btns{display:flex;gap:6px;margin-top:10px}
.btn{font-size:6.5px;font-weight:700;padding:5px 12px;display:inline-block}
.btn-ghost{border:1px solid var(--white);color:var(--white)}
.btn-orange{background:var(--orange);color:var(--white)}
.arrow{position:absolute;top:86px}
.search-band{background:var(--dark);height:80px;position:relative}
.tabs{position:absolute;top:-12px;left:70px;display:flex;font-size:6.5px;font-weight:600}
.tabs span{background:var(--white);padding:6px 12px}
.tabs .on{background:var(--orange);color:var(--white)}
.fields{position:absolute;top:30px;left:70px;display:flex;gap:8px;align-items:center}
.field{width:62px;height:14px;background:#3a3a3a;color:#999;font-size:5.5px;padding:4px}
.welcome{text-align:center;padding-top:18px}
.welcome h2{font-size:12px;font-weight:600}
.welcome p{font-size:6px;color:var(--grey);margin-top:4px}
.welcome .mark{width:8px;height:8px;background:#999;margin:6px auto 0}

/* Books panel */
.books{left:555px;width:200px}
.formats{display:flex;padding:14px 8px;height:96px}
.formats div{flex:1;text-align:center;font-size:5px;color:var(--grey);line-height:1.4;padding:0 4px}
.formats h3{font-size:7.5px;color:var(--ink);margin-bottom:4px}
.formats .alt h3{color:var(--orange)}
.formats .more{display:block;margin-top:8px;color:var(--ink);font-weight:600}
.top-books{background:var(--dark);height:344px;padding:18px 10px;color:var(--white);text-align:center}
.top-books h3{font-size:10px;font-weight:600}
.top-books small{font-size:5px;color:#aaa}
.filter{display:flex;margin:14px 0 14px;font-size:5.5px}
.filter span{background:var(--white);color:var(--ink);padding:6px 8px}
.filter .on{background:var(--orange);color:var(--white)}
.cards{display:flex;gap:6px}
.card{background:var(--white);color:var(--ink);flex:1;padding:6px 6px 8px;text-align:center}
.cover{height:80px;margin-bottom:6px}
.card b{font-size:6.5px;display:block}
.card em{font-style:normal;font-size:5px;color:var(--grey);display:block}
.card strong{font-size:8px;display:block;margin-top:3px}

/* Popular panel */
.popular{left:770px;width:200px}
.collection{background:var(--dark);color:var(--white);height:70px;padding:14px 10px;text-align:center}
.collection h3{font-size:10px;font-weight:600}
.collection p{font-size:5px;color:#bbb;margin:2px 0 6px}
.collection .learn{background:var(--white);color:var(--ink);font-size:5px;padding:3px 8px;display:inline-block}
.pop-head{text-align:center;padding:16px 10px 0}
.pop-head h3{font-size:10px;font-weight:700}
.pop-head p{font-size:5px;color:var(--grey)}
.pop-tabs{display:flex;justify-content:center;gap:4px;margin:10px 0;font-size:5px}
.pop-tabs span{padding:5px 8px;background:var(--light)}
.pop-tabs .on{background:var(--orange);color:var(--white)}
.feature{margin:6px 10px;border:1px solid #e2e2e2;display:flex;gap:8px;padding:8px;box-shadow:0 2px 6px rgba(0,0,0,.08)}
.feature .cover{width:58px;height:86px;margin:0;flex:none}
.feature h4{font-size:7px}
.feature .by{font-size:5px;color:var(--grey)}
.stars{color:var(--ink);font-size:6px;letter-spacing:1px}
.feature p{font-size:4.8px;color:var(--grey);line-height:1.45;margin-top:3px}
.feature .row{display:flex;justify-content:space-between;align-items:center;margin-top:6px}
.feature .row strong{font-size:8px}
.feature .row span{font-size:5px}
.pop-foot{position:absolute;left:0;right:0;bottom:0;height:120px;background:linear-gradient(180deg,#3a322b,#1f1d1b);color:var(--white);padding:10px;font-size:5px}
.pop-foot .price{display:inline-block;background:var(--white);color:var(--ink);font-weight:700;font-size:7px;padding:4px 10px;margin-top:4px}

/* Testimonial panel */
.story{left:985px;width:200px}
.video{height:150px;background:
  radial-gradient(ellipse at 40% 45%,rgba(140,105,80,.55),transparent 55%),
  linear-gradient(135deg,#4a3b30,#241d18 70%);position:relative;color:var(--white);text-align:center}
.video svg{position:absolute;left:88px;top:30px}
.video blockquote{position:absolute;top:64px;left:8px;right:8px;font-size:7px;font-weight:500;line-height:1.3}
.video cite{position:absolute;top:88px;left:0;right:0;font-style:normal;font-size:5px}
.stats{background:var(--orange);display:flex;height:86px;color:var(--white)}
.stat{flex:1;display:flex;flex-direction:column;align-items:center;justify-content:center;gap:5px;font-size:4.8px;text-align:center}
.stat:nth-child(even){background:var(--orange-deep)}
.ring{width:26px;height:26px;border-radius:50%;border:1.5px solid rgba(255,255,255,.85);display:flex;align-items:center;justify-content:center;font-size:6.5px;font-weight:600}
.blog{text-align:center;padding-top:14px}
.blog h3{font-size:9px;font-weight:700}
.blog p{font-size:5px;color:var(--grey)}
.blog .mark{width:6px;height:6px;background:#999;margin:5px auto}
.thumbs{display:flex;gap:4px;padding:8px 8px 0}
.thumbs div{flex:1;height:44px}
</style>
</head>
<body>

<section class="panel home">
  <div class="topbar">
    <span>Welcome To The Amber Ridge Publishing</span>
    <div class="contact">
      <span>hello@amberridgepub.com</span>
      <div class="social"><i></i><i></i><i></i><i></i></div>
    </div>
  </div>
  <nav class="nav">
    <div class="brand"><i></i>AMBER RIDGE<br>PUBLISHING</div>
    <div class="menu">
      <span class="active">HOME</span><span>BOOKS</span><span>TEXT BOOK</span><span>AUDIOBOOKS</span><span>MAGAZINES</span><span>PAGES</span><span>BLOG</span><span>CONTACT US</span>
    </div>
    <div class="menu-search"></div>
  </nav>
  <header class="hero" role="img" aria-label="Photo of books on a bookstore display">
    <svg class="arrow" style="left:20px" width="8" height="14"><path d="M7 1 1 7l6 6" fill="none" stroke="#fff" stroke-width="1"/></svg>
    <svg class="arrow" style="right:20px" width="8" height="14"><path d="M1 1l6 6-6 6" fill="none" stroke="#fff" stroke-width="1"/></svg>
    <div class="hero-inner">
      <div class="kicker">Are You Searching a book publisher...?</div>
      <h1>CUSTOM BOOK PRINTING</h1>
      <p>From printing to promotion, we help you become a published author with care.</p>
      <div class="btns"><span class="btn btn-ghost">SEE MORE</span><span class="btn btn-orange">BUY NOW</span></div>
    </div>
  </header>
  <div class="search-band">
    <div class="tabs"><span>Basic</span><span class="on">Author</span><span>Publications</span></div>
    <div class="fields">
      <div class="field">First Name</div><div class="field">Middle Name</div><div class="field">Last Name</div>
      <span class="btn btn-orange" style="margin-left:20px">SEARCH AUTHOR</span>
    </div>
  </div>
  <div class="welcome">
    <h2>Welcome to the Amber Ridge Publishing</h2>
    <p>Publishing your book is a journey. Let us be your guide.</p>
    <div class="mark"></div>
  </div>
</section>

<section class="panel books">
  <div class="formats">
    <div><h3>Printed Books</h3>Whether you need 50 books or 50,000, we print them with care.<span class="more">See More</span></div>
    <div class="alt"><h3>Ebooks</h3>Reach readers on every device with a digital edition.<span class="more">See More</span></div>
  </div>
  <div class="top-books">
    <h3>Our Top Books</h3>
    <small>Sed ut perspiciatis unde omnis iste natus</small>
    <div class="filter"><span>&larr;</span><span>Arts &amp; Photography</span><span class="on">Mystery</span></div>
    <div class="cards">
      <div class="card"><div class="cover" role="img" aria-label="Book cover of Silent Ledger" style="background:radial-gradient(ellipse at 50% 60%,#3b57b8,transparent 65%),linear-gradient(160deg,#1f2f6b,#0d1233)"></div><b>Silent Ledger</b><em>By M.R. Theodor</em><strong>$18.95</strong></div>
      <div class="card"><div class="cover" role="img" aria-label="Book cover of Harvest" style="background:radial-gradient(ellipse at 50% 70%,#7d8a4f,transparent 60%),linear-gradient(160deg,#6b5a3a,#2f2a20)"></div><b>Harvest</b><em>By Ravi Mehta</em><strong>$35.00</strong></div>
    </div>
  </div>
</section>

<section class="panel popular">
  <div class="collection">
    <h3>Checkout Huge Collection</h3>
    <p>Sed ut perspiciatis unde omnis iste natus</p>
    <span class="learn">Learn More</span>
  </div>
  <div class="pop-head">
    <h3>Most Popular Books</h3>
    <p>Sed ut perspiciatis unde omnis iste natus</p>
  </div>
  <div class="pop-tabs"><span class="on">New Releases</span><span>Best Sellers</span></div>
  <div class="feature">
    <div class="cover" role="img" aria-label="Book cover of Weekend Table" style="background:radial-gradient(ellipse at 60% 75%,#c79a78,transparent 55%),linear-gradient(160deg,#e3e6e8,#8e9aa3)"></div>
    <div>
      <h4>Weekend Table</h4>
      <div class="by">Lena Hartwell</div>
      <div class="stars">&#9733;&#9733;&#9733;&#9733;&#9733;</div>
      <p>Sed ut perspiciatis unde omnis iste natus error sit voluptatem accusantium doloremque laudantium totam rem.</p>
      <div class="row"><strong>$29.95</strong><span>See More</span></div>
    </div>
  </div>
  <div class="pop-foot" role="img" aria-label="Photo of a reader in a library">
    Sed ut perspiciatis unde omnis<br>
    <span class="price">$7.99</span>
  </div>
</section>

<section class="panel story">
  <div class="video" role="img" aria-label="Photo of a reader in a library">
    <svg width="24" height="24" viewBox="0 0 24 24"><circle cx="12" cy="12" r="11" fill="#fff"/><path d="M10 8l6 4-6 4z" fill="#222"/></svg>
    <blockquote>Awesome Design And Great Support! Highly Recommend.</blockquote>
    <cite>Amber Ridge Publishing</cite>
  </div>
  <div class="stats">
    <div class="stat"><div class="ring">14</div>Working Year</div>
    <div class="stat"><div class="ring">1550</div>Books Sold</div>
    <div class="stat"><div class="ring">210</div>Top Author</div>
    <div class="stat"><div class="ring">750</div>Book Published</div>
  </div>
  <div class="blog">
    <h3>Latest Blog Post</h3>
    <p>Sed ut perspiciatis unde omnis iste natus</p>
    <div class="mark"></div>
  </div>
  <div class="thumbs">
    <div role="img" aria-label="Blog photo of a reading desk" style="background:linear-gradient(150deg,#a8957f,#6e604f)"></div>
    <div role="img" aria-label="Blog photo of open books" style="background:linear-gradient(150deg,#d4cfc6,#9c958a)"></div>
    <div role="img" aria-label="Blog photo of a bookshelf" style="background:linear-gradient(150deg,#8a837a,#4f4a44)"></div>
    <div role="img" aria-label="Blog photo of a book display" style="background:linear-gradient(150deg,#e0dbd1,#b0aa9e)"></div>
  </div>
</section>

</body>
</html>
```